Process Roadmap for Interior Design Firm

We are looking to ramp up the design appeal of our current process roadmap to be very visually interesting, while staying informative and descriptive about our process.

Target Market(s)

In-house Clients

Industry/Entity Type

Interior Design Firm focused on sustainable and holistic design.

Other font styles liked:
• raleway

Requirements
Must have
• 1.) it would be nice if the graphic provided a more clear indication of the “journey” from one step to the next, so that there was a clear sense of the progression (such that we are directing the viewer) 2.). We would want it to fit on an 8.5”x11” page (the page could be horizontal when we have the Calm Compass formatted out with the testimonials) (in addition to the testimonials, we may also want to have the detailed descriptions of each step of the process presented below the graphic, so that the graphic is cleaner) 3.) ideally the graphic is clear and simple enough to also be used on our Bi-Weekly Client Updates, which will be typed updates for clients re their project budgets, schedule and scope. The Calm Compass graphic (without all the testimonials) would be at the end of the update, and would fit on the page horizontally at the bottom, perhaps in a space which is 7.5”w x 4”h or so.
Should not have
• bold or bright colors. Natural neutrals are preferred, such as the ones featured on the provided graphic.

```html
<!DOCTYPE html>
<html lang="en">
<head>
<meta charset="utf-8">
<title>The Calm Compass</title>
<link href="https://fonts.googleapis.com/css2?family=Roboto:ital,wght@0,300;0,400;0,500;0,700;1,400&family=Roboto+Condensed:wght@500;700&display=swap" rel="stylesheet">
<style>
  :root {
    --sand-top: #ccbca6;
    --sand-bottom: #b6a488;
    --path: #e4ddd1;
    --bronze: #b07d47;
    --charcoal: #545454;
    --white: #ffffff;
    --quote-grey: #8c8c8c;
    --name-ink: #2f2f2f;
  }
  * { margin: 0; padding: 0; box-sizing: border-box; }
  html, body { width: 1200px; height: 927px; overflow: hidden; background: var(--white); }
  .sheet {
    position: relative;
    width: 1200px; height: 927px;
    overflow: hidden;
    background: linear-gradient(180deg, var(--sand-top) 0%, var(--sand-top) 45%, var(--sand-bottom) 82%);
    font-family: "Roboto", Arial, sans-serif;
  }
  .artwork { position: absolute; inset: 0; }

  .brand-box {
    position: absolute; left: 44px; top: 26px; width: 226px; height: 101px;
    background: var(--white);
    display: flex; align-items: center; justify-content: center; gap: 10px;
  }
  .brand-mark { width: 12px; height: 12px; background: var(--charcoal); }
  .brand-name {
    font-family: "Roboto", Arial, sans-serif; font-weight: 500;
    font-size: 18px; color: var(--charcoal);
  }

  .page-title {
    position: absolute; left: 620px; top: 44px;
    font-size: 49px; font-weight: 400; color: var(--charcoal);
    white-space: nowrap; line-height: 1.1;
  }
  .page-title strong { font-weight: 700; }

  .step-label {
    position: absolute; top: 294px; width: 140px; margin-left: -70px; text-align: center;
    font-weight: 700; font-size: 20px; color: var(--charcoal);
  }

  .step-detail { position: absolute; top: 484px; }
  .step-number {
    font-size: 52px; line-height: 1; color: var(--bronze); font-weight: 300;
    letter-spacing: -1px; margin-left: -4px;
  }
  .step-number b { font-weight: 700; }
  .step-copy {
    margin-top: 4px;
    font-family: "Roboto Condensed", "Arial Narrow", sans-serif; font-weight: 500;
    font-size: 12.4px; line-height: 15.5px; color: var(--white); text-transform: uppercase;
  }
  .step-copy p + p::before {
    content: ""; display: block; width: 22px; height: 1.5px; background: var(--bronze);
    margin: 3px 0 6px;
  }

  .testimonials-title {
    position: absolute; left: 52px; top: 720px;
    font-size: 27px; font-weight: 700; letter-spacing: 1px; color: var(--bronze);
  }
  .testimonial {
    position: absolute; top: 775px; width: 260px;
    font-size: 14px; font-weight: 300; line-height: 16.3px; color: var(--quote-grey);
  }
  .testimonial cite {
    display: block; font-style: italic; font-weight: 400; color: var(--name-ink); margin-top: 2px;
  }
</style>
</head>
<body>
<main class="sheet">
  <svg class="artwork" width="1200" height="927" viewBox="0 0 1200 927" aria-hidden="false">
    <g stroke="var(--bronze)" stroke-width="2">
      <line x1="0" y1="75" x2="44" y2="75"/>
      <line x1="270" y1="75" x2="606" y2="75"/>
      <line x1="1150" y1="75" x2="1200" y2="75"/>
    </g>

    <!-- step connector -->
    <polyline class="step-connector" fill="none" stroke="var(--path)" stroke-width="6" stroke-linejoin="round"
      points="70,375 153,375 301,240 449,375 600,240 749,375 898,240 1050,375 1120,375"/>
    <polygon points="1120,365 1138,375 1120,385" fill="var(--path)"/>

    <!-- step icon areas -->
    <g class="step-icon" fill="var(--path)">
      <circle cx="153" cy="375" r="38" role="img" aria-label="Listening icon"/>
      <circle cx="301" cy="240" r="38" role="img" aria-label="Visioning icon"/>
      <circle cx="449" cy="375" r="38" role="img" aria-label="Planning icon"/>
      <circle cx="600" cy="240" r="38" role="img" aria-label="Designing icon"/>
      <circle cx="749" cy="375" r="38" role="img" aria-label="Managing icon"/>
      <circle cx="898" cy="240" r="38" role="img" aria-label="Installing icon"/>
      <circle cx="1050" cy="375" r="38" role="img" aria-label="Completing icon"/>
    </g>

    <path d="M0 700 H292 Q316 700 330 716 L357 745 H1070 Q1195 745 1200 600 V927 H0 Z" fill="var(--white)"/>
  </svg>

  <div class="brand-box">
    <span class="brand-mark"></span>
    <span class="brand-name">Ada Linwood Design</span>
  </div>

  <h1 class="page-title"><strong>THE</strong> CALM COMPASS</h1>

  <div class="step-label" style="left:153px">Listening</div>
  <div class="step-label" style="left:301px">Visioning</div>
  <div class="step-label" style="left:449px">Planning</div>
  <div class="step-label" style="left:600px">Designing</div>
  <div class="step-label" style="left:749px">Managing</div>
  <div class="step-label" style="left:898px">Installing</div>
  <div class="step-label" style="left:1050px">Completing</div>

  <section class="step-detail" style="left:66px;width:150px">
    <div class="step-number">0<b>1</b></div>
    <div class="step-copy">
      <p>Listening to our clients their land, and their home.</p>
      <p>Identifying their needs, challenges, wishes, and dreams.</p>
    </div>
  </section>
  <section class="step-detail" style="left:230px;width:145px">
    <div class="step-number">0<b>2</b></div>
    <div class="step-copy">
      <p>Facilitating a guided visioning process to clarify the deepest intention, true purpose, and highest potential for their home and their future within it.</p>
    </div>
  </section>
  <section class="step-detail" style="left:382px;width:145px">
    <div class="step-number">0<b>3</b></div>
    <div class="step-copy">
      <p>Turning our client’s vision into a clearly defined scope, budget and timeline.</p>
      <p>Mapping out the steps for making their dream a reality.</p>
      <p>Setting a meeting schedule from start to finish.</p>
    </div>
  </section>
  <section class="step-detail" style="left:534px;width:150px">
    <div class="step-number">0<b>4</b></div>
    <div class="step-copy">
      <p>Following the schedule through the design phases, from initial design concepts, technical drawings and details, and the selection of all finishes, fixtures and furnishings.</p>
    </div>
  </section>
  <section class="step-detail" style="left:694px;width:140px">
    <div class="step-number">0<b>5</b></div>
    <div class="step-copy">
      <p>Coordinating with clients, builders, architects and vendors, to ensure that the design is executed with excellence, and the construction and the furnishings are on-time and on-budget.</p>
    </div>
  </section>
  <section class="step-detail" style="left:847px;width:148px">
    <div class="step-number">0<b>6</b></div>
    <div class="step-copy">
      <p>Overseeing the inspection, installation and arrangements of all furnishings, lighting, artwork and decorative items.</p>
      <p>Taking care of every last detail.</p>
    </div>
  </section>
  <section class="step-detail" style="left:1002px;width:150px">
    <div class="step-number">0<b>7</b></div>
    <div class="step-copy">
      <p>Fixing any issues or defects.</p>
      <p>Follow up on all remaining items.</p>
      <p>Completing the final finishing touches to our client’s full and total satisfaction.</p>
    </div>
  </section>

  <h2 class="testimonials-title">TESTIMONIALS</h2>

  <blockquote class="testimonial" style="left:52px">“Lorem ipsum dolor sit amet, consectetuer adipiscing elit, sed diam nonummy nibh euismod tincidunt ut laoreet dolore magna aliquam erat volutpat. Ut wisi enim ad minim veniam, quis nostrud exerci tation ullamcorper.”<cite>John Doe</cite></blockquote>
  <blockquote class="testimonial" style="left:330px">“Lorem ipsum dolor sit amet, consectetuer adipiscing elit, sed diam nonummy nibh euismod tincidunt ut laoreet dolore magna aliquam erat volutpat. Ut wisi enim ad minim veniam, quis nostrud exerci tation ullamcorper.”<cite>John Doe</cite></blockquote>
  <blockquote class="testimonial" style="left:616px">“Lorem ipsum dolor sit amet, consectetuer adipiscing elit, sed diam nonummy nibh euismod tincidunt ut laoreet dolore magna aliquam erat volutpat. Ut wisi enim ad minim veniam, quis nostrud exerci tation ullamcorper.”<cite>John Doe</cite></blockquote>
  <blockquote class="testimonial" style="left:889px">“Lorem ipsum dolor sit amet, consectetuer adipiscing elit, sed diam nonummy nibh euismod tincidunt ut laoreet dolore magna aliquam erat volutpat. Ut wisi enim ad minim veniam, quis nostrud exerci tation ullamcorper.”<cite>John Doe</cite></blockquote>
</main>
</body>
</html>
```